Lantern Method of Ascent Programme Graphic

Please refer to attached graphic.
I wish to redesign this graphic to represent a programme of work that we (Vendro) deliver to our customers.
The design represents 9 steps ( 3 steps at each of 3 levels) and is all about implementing the 'Lantern Method of Ascent'

I like the fact that the increasing business growth is evident when you are progressing through the stages, but the current graphic looks dated and the colours are not working.
I would also like to incorporate the LMA logo we have created.

Target Market(s)

IT Sector - businesses looking to grow

Industry/Entity Type

We are a digital marketing company

Requirements
Must have
• Clear, concise design
Should not have
• Design must not be complicated

```html
<!DOCTYPE html>
<html lang="en">
<head>
<meta charset="utf-8">
<title>Lantern Method of Ascent Programme</title>
<link href="https://fonts.googleapis.com/css2?family=Oswald:wght@500;600&family=Montserrat:wght@700;800&display=swap" rel="stylesheet">
<style>
  :root {
    --sky-light: #e4f4ff;
    --sky: #9ed8fb;
    --sky-edge: #7fc8f6;
    --column-top: #1560bd;
    --column-bottom: #22205a;
    --step-one: #1493d3;
    --step-two-flag: #4a6db8;
    --step-two-band: #7b9dcb;
    --step-three: #1a98e8;
    --ring-light: #1f8be0;
    --ring-dark: #1d3f9a;
    --tab: #1d8fd6;
    --tab-shade: #1264a8;
    --base: #1494d2;
    --gold-light: #f1cf55;
    --gold: #d9a92b;
    --gold-dark: #b98b12;
    --ink-white: #ffffff;
    --ink-navy: #17367d;
    --ink-brand: #1566c9;
  }
  html, body {
    margin: 0;
    padding: 0;
    width: 1200px;
    height: 849px;
    overflow: hidden;
    background: var(--sky);
  }
  .canvas {
    display: block;
    width: 1200px;
    height: 849px;
  }
  .step-number {
    font-family: "Montserrat", sans-serif;
    font-weight: 800;
    font-size: 92px;
    fill: var(--ink-white);
  }
  .step-title {
    font-family: "Montserrat", sans-serif;
    font-weight: 800;
    font-size: 37px;
    letter-spacing: 2px;
    fill: var(--ink-white);
  }
  .item-label {
    font-family: "Oswald", sans-serif;
    font-weight: 500;
    font-size: 46px;
    fill: var(--ink-white);
  }
  .base-title {
    font-family: "Oswald", sans-serif;
    font-weight: 500;
    font-size: 33px;
    fill: var(--ink-white);
  }
  .base-subtitle {
    font-family: "Montserrat", sans-serif;
    font-weight: 700;
    font-size: 16px;
    letter-spacing: 0.5px;
    fill: var(--ink-white);
  }
  .plinth-title {
    font-family: "Oswald", sans-serif;
    font-weight: 600;
    font-size: 74px;
    fill: var(--ink-white);
  }
  .plinth-mark {
    font-family: "Oswald", sans-serif;
    font-weight: 600;
    font-size: 46px;
    fill: var(--ink-navy);
  }
  .plinth-brand {
    font-family: "Oswald", sans-serif;
    font-weight: 600;
    font-size: 58px;
    fill: var(--ink-brand);
  }
  .icon { fill: none; stroke: var(--ink-white); stroke-width: 4; stroke-linecap: round; stroke-linejoin: round; }
  .icon-solid { fill: var(--ink-white); }
  .tab-face { fill: var(--tab); }
  .tab-shade { fill: var(--tab-shade); }
</style>
</head>
<body>
<svg class="canvas" viewBox="0 0 1755 1241" preserveAspectRatio="none" xmlns="http://www.w3.org/2000/svg" role="img" aria-label="Lantern Method of Ascent programme: three rising steps">
  <defs>
    <radialGradient id="sky-glow" cx="50%" cy="42%" r="70%">
      <stop offset="0" stop-color="var(--sky-light)"/>
      <stop offset="0.6" stop-color="var(--sky)"/>
      <stop offset="1" stop-color="var(--sky-edge)"/>
    </radialGradient>
    <linearGradient id="column-fill" x1="0" y1="0" x2="0" y2="1">
      <stop offset="0" stop-color="var(--column-top)"/>
      <stop offset="1" stop-color="var(--column-bottom)"/>
    </linearGradient>
    <linearGradient id="ring-fill" x1="0" y1="0" x2="1" y2="0">
      <stop offset="0" stop-color="var(--ring-light)"/>
      <stop offset="0.8" stop-color="var(--ring-light)"/>
      <stop offset="1" stop-color="var(--ring-dark)"/>
    </linearGradient>
    <linearGradient id="gold-fill" x1="0" y1="0" x2="1" y2="0">
      <stop offset="0" stop-color="var(--gold-light)"/>
      <stop offset="0.5" stop-color="var(--gold)"/>
      <stop offset="1" stop-color="var(--gold-light)"/>
    </linearGradient>
    <linearGradient id="floor-fill" x1="0" y1="0" x2="0" y2="1">
      <stop offset="0" stop-color="#ffffff" stop-opacity="0.4"/>
      <stop offset="1" stop-color="#ffffff"/>
    </linearGradient>
    <clipPath id="ring-front">
      <rect x="-900" y="0" width="1800" height="320"/>
    </clipPath>
  </defs>

  <!-- backdrop -->
  <rect class="backdrop" width="1755" height="1241" fill="url(#sky-glow)"/>
  <polygon class="floor" points="0,1241 262,1152 1492,1152 1755,1241" fill="url(#floor-fill)"/>

  <!-- ring behind the columns -->
  <g class="orbit-ring" transform="translate(880 388) rotate(-16.5)">
    <ellipse cx="0" cy="0" rx="770" ry="190" fill="none" stroke="url(#ring-fill)" stroke-width="66"/>
  </g>

  <!-- step columns -->
  <g class="step step-one">
    <polygon points="320,595 640,490 640,935 320,935" fill="url(#column-fill)"/>
    <polygon points="320,398 340,390 522,462 320,532" fill="var(--step-one)"/>
    <polygon points="320,540 640,432 640,490 320,598" fill="var(--step-one)"/>
    <text class="step-number" x="335" y="495">1</text>
    <text class="step-title" x="0" y="0" transform="translate(388 556) rotate(-18.5)">LANTERN</text>
  </g>
  <g class="step step-two">
    <polygon points="720,460 1040,355 1040,935 720,935" fill="url(#column-fill)"/>
    <polygon points="720,263 740,255 918,327 720,397" fill="var(--step-two-flag)"/>
    <polygon points="720,405 1040,297 1040,355 720,463" fill="var(--step-two-band)"/>
    <text class="step-number" x="740" y="355">2</text>
    <text class="step-title" x="0" y="0" transform="translate(778 418) rotate(-18.5)">METHOD</text>
  </g>
  <g class="step step-three">
    <polygon points="1118,315 1438,210 1438,935 1118,935" fill="url(#column-fill)"/>
    <polygon points="1118,138 1138,130 1288,188 1118,250" fill="var(--step-three)"/>
    <polygon points="1118,258 1438,150 1438,210 1118,318" fill="var(--step-three)"/>
    <text class="step-number" x="1130" y="215">3</text>
    <text class="step-title" x="0" y="0" transform="translate(1168 276) rotate(-18.5)">ASCENT</text>
  </g>

  <!-- ring passing in front -->
  <g class="orbit-ring-front" transform="translate(880 388) rotate(-16.5)" clip-path="url(#ring-front)">
    <ellipse cx="0" cy="0" rx="770" ry="190" fill="none" stroke="var(--ring-light)" stroke-opacity="0.82" stroke-width="66"/>
  </g>

  <!-- step items -->
  <g class="step-items">
    <!-- tab shape reused per row -->
    <g class="item" transform="translate(310 687)">
      <polygon class="tab-shade" points="0,0 0,58 10,70 10,10"/>
      <polygon class="tab-face" points="0,0 62,0 74,25 62,50 0,50"/>
      <circle class="icon-solid" cx="20" cy="17" r="6"/><circle class="icon-solid" cx="33" cy="14" r="7"/><circle class="icon-solid" cx="46" cy="17" r="6"/>
      <path class="icon-solid" d="M10 38 q10 -16 20 0 z M22 38 q11 -19 22 0 z M36 38 q10 -16 20 0 z"/>
    </g>
    <text class="item-label" x="393" y="731">PERSONAS</text>

    <g class="item" transform="translate(310 770)">
      <polygon class="tab-shade" points="0,0 0,58 10,70 10,10"/>
      <polygon class="tab-face" points="0,0 62,0 74,25 62,50 0,50"/>
      <ellipse class="icon-solid" cx="34" cy="12" rx="13" ry="5"/>
      <rect class="icon-solid" x="21" y="16" width="26" height="8" rx="3"/>
      <rect class="icon-solid" x="21" y="26" width="26" height="8" rx="3"/>
      <rect class="icon-solid" x="21" y="36" width="26" height="8" rx="3"/>
    </g>
    <text class="item-label" x="393" y="812">DATABASE</text>

    <g class="item" transform="translate(310 853)">
      <polygon class="tab-shade" points="0,0 0,58 10,70 10,10"/>
      <polygon class="tab-face" points="0,0 62,0 74,25 62,50 0,50"/>
      <circle class="icon" cx="34" cy="25" r="14" stroke-dasharray="6 3.5"/>
      <circle class="icon" cx="34" cy="25" r="6"/>
    </g>
    <text class="item-label" x="390" y="896">SYSTEMS</text>

    <g class="item" transform="translate(710 687)">
      <polygon class="tab-shade" points="0,0 0,58 10,70 10,10"/>
      <polygon class="tab-face" points="0,0 62,0 74,25 62,50 0,50" fill="var(--step-two-flag)" style="fill:var(--step-two-flag)"/>
      <path class="icon-solid" d="M16 10 h38 v24 h-16 l-6 8 l-6 -8 h-10 z"/>
      <circle cx="26" cy="22" r="2.5" fill="var(--step-two-flag)"/><circle cx="35" cy="22" r="2.5" fill="var(--step-two-flag)"/><circle cx="44" cy="22" r="2.5" fill="var(--step-two-flag)"/>
    </g>
    <text class="item-label" x="803" y="727">MESSAGING</text>

    <g class="item" transform="translate(710 770)">
      <polygon class="tab-shade" points="0,0 0,58 10,70 10,10"/>
      <polygon points="0,0 62,0 74,25 62,50 0,50" style="fill:var(--step-two-flag)"/>
      <circle class="icon" cx="34" cy="25" r="15" stroke-dasharray="7 3"/>
      <path class="icon" d="M27 25 l5 5 l9 -10"/>
    </g>
    <text class="item-label" x="803" y="812">LEADS</text>

    <g class="item" transform="translate(710 853)">
      <polygon class="tab-shade" points="0,0 0,58 10,70 10,10"/>
      <polygon points="0,0 62,0 74,25 62,50 0,50" style="fill:var(--step-two-flag)"/>
      <path class="icon" stroke-width="6" d="M24 12 h14 a7 7 0 0 1 0 14 h-8 a7 7 0 0 0 0 14 h16"/>
    </g>
    <text class="item-label" x="803" y="896">PIPELINE</text>

    <g class="item" transform="translate(1108 687)">
      <polygon class="tab-shade" points="0,0 0,58 10,70 10,10"/>
      <polygon points="0,0 62,0 74,25 62,50 0,50" style="fill:var(--step-three)"/>
      <path class="icon" d="M16 35 l12 -12 l8 8 l14 -14 M40 16 h10 v10"/>
    </g>
    <text class="item-label" x="1203" y="727">SALES</text>

    <g class="item" transform="translate(1108 770)">
      <polygon class="tab-shade" points="0,0 0,58 10,70 10,10"/>
      <polygon points="0,0 62,0 74,25 62,50 0,50" style="fill:var(--step-three)"/>
      <path class="icon-solid" d="M33 30 q-14 2 -16 -12 q14 -2 16 12 z M35 24 q2 -14 16 -14 q0 14 -16 14 z"/>
      <rect class="icon-solid" x="32" y="22" width="4" height="14"/>
      <rect class="icon-solid" x="23" y="34" width="22" height="10" rx="2"/>
    </g>
    <text class="item-label" x="1203" y="812">NURTURE</text>

    <g class="item" transform="translate(1108 853)">
      <polygon class="tab-shade" points="0,0 0,58 10,70 10,10"/>
      <polygon points="0,0 62,0 74,25 62,50 0,50" style="fill:var(--step-three)"/>
      <path class="icon" d="M22 10 h16 l8 8 v24 h-24 z M29 28 h10 M35 23 l5 5 l-5 5"/>
    </g>
    <text class="item-label" x="1203" y="896">REFERENCE</text>
  </g>

  <!-- column bases -->
  <g class="column-bases">
    <polygon points="305,945 315,935 640,935 650,945" fill="var(--tab-shade)"/>
    <rect x="305" y="945" width="345" height="78" fill="var(--base)"/>
    <text class="base-title" x="480" y="984" text-anchor="middle">NUMBERS THAT MATTER</text>
    <text class="base-subtitle" x="480" y="1007" text-anchor="middle">FOUNDATION METRICS</text>

    <polygon points="705,945 715,935 1040,935 1050,945" fill="var(--tab-shade)"/>
    <rect x="705" y="945" width="345" height="78" fill="var(--base)"/>
    <text class="base-title" x="880" y="984" text-anchor="middle">WEEKLY SCORECARD</text>
    <text class="base-subtitle" x="880" y="1007" text-anchor="middle">TACTICAL EXECUTION</text>

    <polygon points="1104,945 1114,935 1439,935 1449,945" fill="var(--tab-shade)"/>
    <rect x="1104" y="945" width="345" height="78" fill="var(--base)"/>
    <text class="base-title" x="1277" y="982" text-anchor="middle">MONTHLY SCORECARD</text>
    <text class="base-subtitle" x="1277" y="1007" text-anchor="middle">STRATEGIC REVIEW</text>
  </g>

  <!-- plinth -->
  <g class="plinth">
    <polygon points="262,1048 290,1022 1462,1022 1492,1048" fill="var(--gold-dark)"/>
    <rect x="262" y="1048" width="1230" height="104" fill="url(#gold-fill)"/>
    <rect x="270" y="1055" width="1214" height="90" fill="none" stroke="#fff3c2" stroke-width="2"/>
    <text class="plinth-mark" x="282" y="1118">LMA</text>
    <text class="plinth-title" x="383" y="1127" textLength="880" lengthAdjust="spacingAndGlyphs">LANTERN METHOD OF ASCENT</text>
    <text class="plinth-brand" x="1282" y="1124" textLength="190" lengthAdjust="spacingAndGlyphs">VENDRO</text>
  </g>
</svg>
</body>
</html>
```